new marketing company logo and business card

design logo and biz card for marketing start up.

My company name needs a brand logo designed: Copper Lantern Marketing Co.
Tagline: Sales - Marketing - Brand Building

Sister Bay is the name of my favorite place, in Wisconsin, but the business is NOT BASED there. It should evoke warmth, friendliness, professionalism, and marketing services from a seasoned marketer.

Target Market(s)

I am selling my services to small business that need help.

Industry/Entity Type

Marketing

Contact Information for Business Card

Copper Lantern Marketing Co. (logo)
Sales - Marketing - Brand Building (tagline)

Dana M. Whitcombe
DanaMWhitcombe@fernlymail.com
555-384-0192 mobile

Font styles to use
Serif
Sans Serif

Colors
f78f20
f37122
f68d4d
00a990
85cae6
33b8a4
faa54b

Requirements
Must have
• a logo
• a business card
Nice to have
• I'd love to see a small subtle reference to Sister Bay built in. Sister bay is named that because there are two islands called ‘sister islands’ that flank the bay. If you google this you will see.
• I like warm, earthy colors. But, I am a fun, approachable, real person. Not stand-offish. Should be warm and appealing yet professional.
Should not have
• nothing cartoon-ish. no child-like fonts. this is a professional business.

```html
<!DOCTYPE html>
<html lang="en">
<head>
<meta charset="utf-8">
<title>Copper Lantern Marketing Co. – Business Card</title>
<link href="https://fonts.googleapis.com/css2?family=Libre+Baskerville&family=Montserrat:wght@400;600&display=swap" rel="stylesheet">
<style>
  :root {
    --stage: #1c1c1c;
    --card: #ffffff;
    --orange: #f37122;
    --orange-soft: #f78f20;
    --teal: #00a990;
    --ink: #2b2b2b;
    --grey: #4a4a4a;
  }
  * { box-sizing: border-box; margin: 0; padding: 0; }
  html, body { width: 1200px; height: 900px; overflow: hidden; background: var(--stage); }
  .stage { position: relative; width: 1200px; height: 900px; }
  .card {
    position: absolute; width: 580px; height: 330px; background: var(--card);
    box-shadow: 0 18px 40px rgba(0,0,0,.55);
  }
  /* Front */
  .card-front { left: 100px; top: 80px; font-family: "Libre Baskerville", serif; }
  .front-brand { position: absolute; left: 0; right: 0; top: 46px; text-align: center; }
  .brand-mark { display: block; border-radius: 50%; background: var(--orange-soft); }
  .front-mark { width: 58px; height: 58px; margin: 0 auto 16px; }
  .front-name { color: var(--teal); font-size: 27px; line-height: 1.15; letter-spacing: .5px; text-transform: uppercase; }
  .front-rule { width: 250px; height: 1px; background: var(--orange-soft); margin: 12px auto 10px; }
  .front-tagline { color: var(--orange-soft); font-family: "Montserrat", sans-serif; font-size: 11px; letter-spacing: 1px; text-transform: uppercase; }
  .front-web { position: absolute; left: 0; right: 0; bottom: 40px; text-align: center; font-family: "Montserrat", sans-serif; font-size: 13px; color: var(--ink); }
  .front-web b { color: var(--teal); font-weight: 600; }
  /* Back */
  .card-back { left: 520px; top: 490px; font-family: "Montserrat", sans-serif; }
  .back-brand { position: absolute; left: 34px; top: 72px; width: 240px; }
  .back-mark { width: 48px; height: 48px; margin: 0 0 14px 70px; background: var(--orange); }
  .back-name { color: var(--orange); font-size: 25px; line-height: 1.1; text-transform: uppercase; font-weight: 400; }
  .back-tagline { margin-top: 10px; color: var(--ink); font-size: 12px; }
  .rule { position: absolute; height: 1px; background: var(--orange); }
  .rule-top { left: 282px; right: 0; top: 44px; }
  .rule-mid { left: 282px; right: 0; top: 110px; }
  .rule-low { left: 282px; right: 40px; top: 186px; }
  .person { position: absolute; left: 282px; top: 62px; }
  .person-name { color: var(--orange); font-size: 21px; letter-spacing: 1px; text-transform: uppercase; }
  .person-title { color: var(--ink); font-size: 12px; font-weight: 600; margin-top: 4px; }
  .address { position: absolute; left: 296px; top: 124px; color: var(--grey); font-size: 12px; line-height: 1.4; }
  .contacts { position: absolute; left: 296px; top: 198px; list-style: none; color: var(--grey); font-size: 12px; }
  .contacts li { display: flex; align-items: center; gap: 8px; line-height: 1.55; }
  .contacts svg { width: 11px; height: 11px; flex: none; }
</style>
</head>
<body>
<main class="stage">
  <section class="card card-front">
    <div class="front-brand">
      <span class="brand-mark front-mark" aria-hidden="true"></span>
      <div class="front-name">Copper Lantern<br>Marketing Co.</div>
      <div class="front-rule"></div>
      <div class="front-tagline">Sales - Marketing - Brand Building</div>
    </div>
    <div class="front-web">www.<b>larchfieldpartners</b>.com</div>
  </section>

  <section class="card card-back">
    <div class="rule rule-top"></div>
    <div class="back-brand">
      <span class="brand-mark back-mark" aria-hidden="true"></span>
      <div class="back-name">Copper Lantern<br>Marketing Co.</div>
      <div class="back-tagline">Sales - Marketing - Brand Building</div>
    </div>
    <div class="person">
      <div class="person-name">Marlo Finchley</div>
      <div class="person-title">Vice President</div>
    </div>
    <div class="rule rule-mid"></div>
    <div class="address">742 Alder Row<br>Suite 310<br>Brookhaven, OR 97000</div>
    <div class="rule rule-low"></div>
    <ul class="contacts">
      <li><svg viewBox="0 0 12 12"><path d="M2 1h2.5l1 3-1.5 1a6 6 0 0 0 3 3l1-1.5 3 1V10a1 1 0 0 1-1 1A9 9 0 0 1 1 2a1 1 0 0 1 1-1z" fill="var(--orange)"/></svg>555 - 210 - 4471</li>
      <li><svg viewBox="0 0 12 12"><rect x="3" y="1" width="6" height="10" rx="1" fill="none" stroke="var(--orange)" stroke-width="1.3"/><circle cx="6" cy="9" r=".7" fill="var(--orange)"/></svg>555-618-2290</li>
      <li><svg viewBox="0 0 12 12"><rect x="1" y="5" width="10" height="6" rx="1" fill="var(--orange)"/><rect x="3" y="1" width="6" height="4" fill="none" stroke="var(--orange)" stroke-width="1.2"/></svg>555 - 210 - 4471</li>
      <li><svg viewBox="0 0 12 12"><rect x="1" y="2.5" width="10" height="7" fill="none" stroke="var(--orange)" stroke-width="1.2"/><path d="M1 2.5l5 4 5-4" fill="none" stroke="var(--orange)" stroke-width="1.2"/></svg>marlo@larchfieldpartners.com</li>
    </ul>
  </section>
</main>
</body>
</html>
```